WP website design for Dorrance

We need a wordpress design that will incorporate a professional color scheme with company logo in a clean layout. The design needs to consider that this will be developed on a responsive theme. Colors are will be the green of the logo and any others that will creatively highlight it.

Industry/Entity Type

It Company

Font styles to use
Sans Serif

Requirements
Must have
• Navigation: 1) Home 2) Auctions 3) Auction Services 4) Sellers 5) KT Dorrance Livestock 6) About Us 7) Contact Us
Site will have slideshow element, image attached.
Widgets will be: 1)Email Signup form 2) Featured Auctions widget 3) Social Media (FB, Youtube, RSS) 4) News & Events blog
Footer will have smaller company logo, association logos (attached) and contact info (below)
▪ K.T. Dorrance Inc. / Auctioneers
▪ 4715 NC Hwy 91
▪ Belmora, NC 27640
▪ Office: (252) 555-0187
▪ Cell: (252) 555-0163
▪ email: ktdorrance@ktdorrance-example.com
Nice to have
• Site will have drop-down menus - please indicate the styling, for instance the dropdown menus

```html
<!DOCTYPE html>
<html lang="en">
<head>
<meta charset="utf-8">
<title>K.T. Dorrance Inc. / Auctioneers</title>
<link href="https://fonts.googleapis.com/css2?family=Open+Sans:wght@400;600;700&display=swap" rel="stylesheet">
<style>
:root{
  --green:#3f8e1f;
  --green-bright:#5cab2b;
  --green-light:#d8f0c4;
  --black:#0c0c0c;
  --dark:#3a3a3a;
  --footer:#303030;
  --grey-text:#5a5a5a;
  --white:#ffffff;
  --orange:#f3a52c;
  --slide-warm:#b3a27c;
  --slide-cool:#9fb0b8;
}
*{margin:0;padding:0;box-sizing:border-box}
html,body{width:758px;height:1200px;overflow:hidden;background:#fff}
body{font-family:"Open Sans",Arial,sans-serif;position:relative;color:var(--grey-text)}
.abs{position:absolute}

/* header */
.site-header{left:0;top:0;width:758px;height:108px;
  background:linear-gradient(180deg,#8a7c64 0%,#a8936c 55%,#6f6a55 100%);border-top:4px solid var(--green)}
.brand{left:73px;top:4px;width:86px;height:88px;background:var(--white);border:2px solid #ddd;
  display:flex;flex-direction:column;align-items:center;justify-content:center;gap:4px}
.brand-mark{width:14px;height:14px;background:var(--green)}
.brand-name{color:var(--green);font-weight:700;font-size:11px;text-align:center;line-height:1.2}
.site-title{left:320px;top:18px;width:210px;text-align:center;line-height:1}
.site-title .t1{color:var(--white);font-size:16px;font-weight:600}
.site-title .t2{color:var(--green-bright);font-size:32px;font-weight:600;margin-top:2px}
.site-title .t2 span{color:var(--white);font-size:28px}
.site-title .t3{color:var(--orange);font-size:28px;font-weight:600;margin-top:2px}
.phone-box{left:556px;top:10px;width:129px;height:19px;background:var(--black);color:var(--white);
  font-size:11px;display:flex;align-items:center;justify-content:center;gap:6px}
.header-social{left:571px;top:40px;display:flex;gap:6px}
.header-social i{display:block;width:16px;height:16px;border-radius:50%;background:#2b2b2b;border:1px solid #777}

/* nav */
.main-nav{left:0;top:108px;width:758px;height:30px;background:var(--black);border-bottom:5px solid var(--green)}
.main-nav a{position:absolute;top:10px;color:var(--white);font-size:8px;text-decoration:none;white-space:nowrap}
.dropdown{left:355px;top:143px;width:183px;height:193px;background:rgba(40,40,40,.85);z-index:3}
.dropdown a{position:absolute;left:22px;color:var(--white);font-size:8.5px;text-decoration:none}

/* slider */
.hero{left:0;top:143px;width:758px;height:346px;background:linear-gradient(180deg,#77736b 0%,#5e5b56 100%)}
.hero-slide{left:73px;top:159px;width:606px;height:312px;border:4px solid var(--black);
  background:linear-gradient(135deg,var(--slide-warm) 0%,var(--slide-cool) 100%);box-shadow:0 0 12px rgba(0,0,0,.6)}
.arrow{top:293px}

/* featured */
.featured{left:0;top:489px;width:758px;height:275px;background:var(--dark)}
.featured h2{position:absolute;left:76px;top:28px;color:var(--white);font-size:17px;font-weight:400}
.featured .lead{position:absolute;left:76px;top:49px;color:var(--white);font-size:8.5px}
.auction-card{position:absolute;top:77px;width:134px}
.auction-card .thumb{height:103px;background:radial-gradient(circle at 50% 45%,#6fb835 0%,#2e6a12 28%,#000 58%)}
.auction-card h3{margin-top:2px;height:20px;background:var(--green);color:var(--white);font-size:9.5px;font-weight:400;padding:4px 6px}
.auction-card p{color:#555;font-size:7.5px;line-height:1.25;padding:6px 1px 0}
.read-more{position:absolute;right:0;top:165px;width:55px;height:12px;background:linear-gradient(#f2f2f2,#bdbdbd);
  color:#333;font-size:6.5px;font-weight:600;text-align:center;line-height:12px}

/* about */
.about{left:31px;top:780px;width:430px}
.about h2{color:#222;font-size:14px;font-weight:400;margin-bottom:8px}
.about p{font-size:7.8px;line-height:1.46;color:#444}
.about-divider{left:479px;top:778px;width:2px;height:178px;background:var(--green-bright)}
.subscribe-panel{left:481px;top:764px;width:277px;height:208px;
  background:linear-gradient(135deg,#ffffff 0%,#e6f1f8 45%,#f8fbfd 60%,#dcecf5 100%)}
.sub-title{color:#222;font-size:11px}
.email-field{background:var(--green-light);border:2px solid #c9c58a;font-size:8.5px;color:#333;padding:4px 8px}
.btn{background:linear-gradient(#ffffff,#bcbcbc);border:1px solid #8a8a8a;color:#111;font-size:8.5px;text-align:center}

/* footer */
.footer-band{left:0;top:972px;width:758px;height:12px;background:var(--green)}
.footer{left:0;top:984px;width:758px;height:190px;background:var(--footer)}
.footer h4{position:absolute;color:var(--white);font-size:11px;font-weight:400}
.partners{left:37px;top:1042px;width:159px;height:58px;background:var(--green);padding:5px;display:flex;gap:4px}
.partners div{flex:1;background:var(--white)}
.footer-social{left:306px;top:1134px;width:165px;height:25px;background:#3c3c3c;display:flex;align-items:center;justify-content:center;gap:7px}
.footer-social i{display:block;width:10px;height:10px;border-radius:50%;background:#777}
.footer-brand{left:548px;top:974px;width:98px;height:69px;background:var(--white);border:3px solid var(--footer);
  display:flex;flex-direction:column;align-items:center;justify-content:center;gap:3px}
.contact{left:551px;top:1060px;color:#bbb;font-size:7.8px}
.contact li{list-style:none;display:flex;gap:10px;margin-bottom:10px;line-height:1.35}
.contact svg{flex:none;margin-top:1px}
.bottom-bar{left:0;top:1174px;width:758px;height:26px;background:#262626;border-top:3px solid var(--green);border-bottom:8px solid var(--green)}
.bottom-bar p{color:#aaa;font-size:7px;padding:3px 0 0 42px}
</style>
</head>
<body>

<header class="abs site-header">
  <div class="abs brand"><span class="brand-mark"></span><span class="brand-name">K.T. Dorrance<br>Inc. / Auctioneers</span></div>
  <div class="abs site-title"><div class="t1">North Carolina</div><div class="t2">Auctions <span>&amp;</span></div><div class="t3">Auctioneering</div></div>
  <div class="abs phone-box">
    <svg width="9" height="9" viewBox="0 0 10 10"><path d="M2 0.5 L3.8 0.5 L4.5 3 L3.2 4 Q4.2 6 6 6.8 L7 5.5 L9.5 6.2 L9.5 8 Q9.5 9.5 8 9.5 Q0.5 9 0.5 2 Q0.5 0.5 2 0.5Z" fill="#fff"/></svg>
    (252) 555-0187</div>
  <div class="abs header-social"><i></i><i></i><i></i><i></i><i></i></div>
</header>

<nav class="abs main-nav">
  <a style="left:318px">Home</a>
  <a style="left:354px">Auctions</a>
  <a style="left:396px">Auction Services</a>
  <a style="left:466px">Sellers</a>
  <a style="left:501px">KT Dorrance Livestock</a>
  <a style="left:601px">About Us</a>
  <a style="left:646px">Contact Us</a>
</nav>

<section class="abs hero"></section>
<div class="abs hero-slide" role="img" aria-label="Slideshow photo of a pond with autumn trees and grassland"></div>
<svg class="abs arrow" style="left:18px" width="26" height="26" viewBox="0 0 26 26"><path d="M24 1 L2 13 L24 25Z" fill="#2e2e2e"/></svg>
<svg class="abs arrow" style="left:710px" width="26" height="26" viewBox="0 0 26 26"><path d="M2 1 L24 13 L2 25Z" fill="#2e2e2e"/></svg>
<div class="abs dropdown">
  <a style="top:44px">Local Auctions</a>
  <a style="top:64px">Latest Auctions</a>
  <a style="top:85px">Auctions Ending Soon</a>
  <a style="top:106px">Auction Terms &amp; Condition</a>
</div>

<section class="abs featured">
  <h2>Featured Auctions</h2>
  <p class="lead">Watchout our new featured auction, dont miss them, they worth fotunes</p>
  <article class="auction-card" style="left:73px"><div class="thumb" role="img" aria-label="Green leaf on black"></div><h3>Auction Heading Here</h3><p>Auction detail with pricing and features and terms &amp; condition and other detail will be appear here</p><span class="read-more">READ MORE</span></article>
  <article class="auction-card" style="left:232px"><div class="thumb" role="img" aria-label="Green leaf on black"></div><h3>Auction Heading Here</h3><p>Auction detail with pricing and features and terms &amp; condition and other detail will be appear here</p><span class="read-more">READ MORE</span></article>
  <article class="auction-card" style="left:389px"><div class="thumb" role="img" aria-label="Green leaf on black"></div><h3>Auction Heading Here</h3><p>Auction detail with pricing and features and terms &amp; condition and other detail will be appear here</p><span class="read-more">READ MORE</span></article>
  <article class="auction-card" style="left:545px"><div class="thumb" role="img" aria-label="Green leaf on black"></div><h3>Auction Heading Here</h3><p>Auction detail with pricing and features and terms &amp; condition and other detail will be appear here</p><span class="read-more">READ MORE</span></article>
</section>

<section class="abs about">
  <h2>North Carolina Auctions and Auctioneering</h2>
  <p>Our auction business was started in 1977. We conduct farm equipment, logging &amp; industrial equipment, real estate, antique &amp; cattle sales.<br>
  K. T. Dorrance, owner/president, was raised on the family farm in Warren County. This farm has been in his family since 1916. The office for the auction business is also located at this farm.<br>
  There were many family values passed on to him which are used in everyday life. Some of these are used in the auction business today. For example - (1) give a man a fair measure (2) look a person straight in the eye &amp; give them a firm hand shake. When you employ K. T. Dorrance Inc./Auctioneers you are dealing with a company known for treating their customers, whether a seller or buyer, with these values.<br>
  We are a name both buyer and seller can trust. If you are considering an auction or buying equipment, be sure to contact us for more information about our services. We always appreciate your business.<br>
  K. T. Dorrance is a member of Auctioneers Guild of the Carolinas, Piedmont Cattle Growers Council and National Grassland Beef Council</p>
</section>
<div class="abs subscribe-panel"></div>
<div class="abs about-divider"></div>
<div class="abs sub-title" style="left:534px;top:818px">Subscribe for Newsletter</div>
<div class="abs email-field" style="left:532px;top:857px;width:161px;height:22px">Email Address</div>
<div class="abs btn" style="left:636px;top:895px;width:57px;height:21px;line-height:19px">Subscribe</div>

<div class="abs footer-band"></div>
<footer class="abs footer">
  <h4 style="left:37px;top:31px">In Association with</h4>
  <h4 style="left:304px;top:31px">Subscribe for Newsletter</h4>
</footer>
<div class="abs partners"><div></div><div></div><div></div></div>
<div class="abs email-field" style="left:303px;top:1054px;width:162px;height:22px">Email Address</div>
<div class="abs btn" style="left:406px;top:1091px;width:59px;height:20px;line-height:18px">Subscribe</div>
<div class="abs footer-social"><i></i><i></i><i></i><i></i><i></i><i></i><i></i><i></i></div>
<div class="abs footer-brand"><span class="brand-mark"></span><span class="brand-name">K.T. Dorrance<br>Inc. / Auctioneers</span></div>
<ul class="abs contact">
  <li><svg width="8" height="8" viewBox="0 0 10 10"><path d="M2 0.5 L3.8 0.5 L4.5 3 L3.2 4 Q4.2 6 6 6.8 L7 5.5 L9.5 6.2 L9.5 8 Q9.5 9.5 8 9.5 Q0.5 9 0.5 2 Q0.5 0.5 2 0.5Z" fill="#999"/></svg>(252) 555-0187</li>
  <li><svg width="8" height="9" viewBox="0 0 8 10"><rect x="1" y="0.5" width="6" height="9" rx="1" fill="none" stroke="#999"/><circle cx="4" cy="8" r=".7" fill="#999"/></svg>(252) 555-0163</li>
  <li><svg width="9" height="7" viewBox="0 0 10 8"><rect x=".5" y=".5" width="9" height="7" fill="none" stroke="#999"/><path d="M.5 .5 L5 4.5 L9.5 .5" fill="none" stroke="#999"/></svg>ktdorrance@ktdorrance-example.com</li>
  <li><svg width="8" height="10" viewBox="0 0 8 10"><path d="M4 10 L1 5 A3.5 3.5 0 1 1 7 5Z" fill="#999"/><circle cx="4" cy="3.5" r="1.2" fill="#303030"/></svg>K.T. Dorrance Inc. / Auctioneers<br>4715 NC Hwy 91<br>Belmora, NC 27640</li>
</ul>
<div class="abs bottom-bar"><p>© 2014 KTDORRANCE-EXAMPLE.com . All rights reserved.</p></div>

</body>
</html>
```